Tax consulting firm needs an advertisment for magazine/book/flyer

NEEDED
We need an advert to promote our general business with the following dimensions:-
230 x 148 + 5mm
PDF, 300 dpi
It is for inclusion in a larger publication - attached is the .pdf guide provided by the publisher with regard to dimensions needed.
The advert may also be used to print flyers in A5/A6 sizes so if it can also be scaled to fit those measurements that would be great.
BACKGROUND
We are a tax firm specialising in Luxembourg, UK and US personal taxes. We would like the advertisement to be in keeping with the feel of the website (www.morvelcount.com) and other material (winning files from previous design contests are attached for style/feel). The advert should be professional, modern, but elegant. Any photographs included should be in B&W and be of Luxembourg City and not of any other cities.
DETAILS
The design should utilise the colours of the brand:-
#7D1935
#4A96AD
#F5F3EE
The text "Specialists in Luxembourg, UK and US personal tax compliance and consulting" should be included and also website address and company logo.
For any questions, please send a message and I will respond as soon as I can.

```html
<!DOCTYPE html>
<html lang="en">
<head>
<meta charset="utf-8">
<title>Morvel Tax & Consulting – Advertisement</title>
<link rel="stylesheet" href="https://fonts.googleapis.com/css2?family=PT+Sans:wght@400;700&display=swap">
<style>
  :root {
    --backdrop: #1c1c1c;
    --brand-maroon: #7d1935;
    --brand-maroon-deep: #6a1029;
    --paper: #ffffff;
    --headline-grey: #8a8a8a;
    --white: #ffffff;
  }
  * { margin: 0; padding: 0; box-sizing: border-box; }
  html, body {
    width: 1200px; height: 1000px; overflow: hidden;
    background: var(--backdrop);
    font-family: "PT Sans", "Myriad Pro", Arial, sans-serif;
  }
  .advert {
    position: absolute; left: 82px; top: 178px;
    width: 1035px; height: 665px;
    background: var(--paper);
    overflow: hidden;
  }
  .brand-panel {
    position: absolute; left: 0; top: 0;
    width: 370px; height: 100%;
    background: var(--brand-maroon);
  }
  .brand-panel__edge {
    position: absolute; right: 0; top: 0;
    width: 20px; height: 100%;
    background: var(--brand-maroon-deep);
  }
  .brand-mark {
    position: absolute; left: 34px; top: 35px;
    display: flex; align-items: center; gap: 18px;
  }
  .brand-mark__dot {
    width: 78px; height: 78px; border-radius: 50%;
    border: 2px solid var(--white);
  }
  .brand-mark__name {
    color: var(--white); font-weight: 400;
    font-size: 44px; line-height: 1; letter-spacing: 1px;
  }
  .brand-mark__name small {
    display: block; font-size: 19px; letter-spacing: 0.5px; margin-top: 2px;
  }
  .contact {
    position: absolute; left: 33px; top: 568px;
    list-style: none; color: var(--white);
    font-size: 14px; line-height: 24.5px;
  }
  .headline {
    position: absolute; left: 495px; top: 92px; width: 460px;
    color: var(--headline-grey); font-weight: 700;
    font-size: 33px; line-height: 44px; letter-spacing: -0.3px;
  }
  .city-photo {
    position: absolute; left: 370px; top: 270px;
    width: 665px; height: 395px;
    background: linear-gradient(to bottom, #ffffff 0%, #e4e4e4 22%, #a8a8a8 45%, #6d6d6d 72%, #3f3f3f 100%);
  }
  .web-address {
    position: absolute; right: 0; bottom: 31px;
    width: 281px; height: 30px;
    background: var(--brand-maroon);
    color: var(--white); font-weight: 700; font-size: 22px;
    line-height: 30px; text-align: center;
  }
</style>
</head>
<body>
  <div class="advert">
    <aside class="brand-panel">
      <div class="brand-panel__edge"></div>
      <div class="brand-mark">
        <span class="brand-mark__dot"></span>
        <span class="brand-mark__name">MORVEL<small>TAX &amp; CONSULTING</small></span>
      </div>
      <ul class="contact">
        <li>Email: enquiries@morvelcount.com</li>
        <li>Talkline ID: Morvel.count</li>
        <li>Tel (Lux): +352 20 41 57 93</li>
      </ul>
    </aside>
    <h1 class="headline">Specialists in Luxembourg, UK and US personal tax compliance and consulting</h1>
    <div class="city-photo" role="img" aria-label="Black and white photograph of Luxembourg City old town rooftops below the fortress cliffs and church spires"></div>
    <div class="web-address">www.morvelcount.com</div>
  </div>
</body>
</html>
```